zunTRAK Company Website
Technology Solutions and Consulting
Project: zunTRAK Company Website
zunTRAK Company Website - Information Technology
Creative Brief
Information Technology
www.zuntrak.net
We offer Technology, Telecom Services, Solutions and Consulting for enterprise level businesses. Specializing but not limited to telecom related businesses. zunTRAK is an integrated business development solution company that provides technology integration, advisory services, infrastructure to enterprises and SME to boost their leads, sales and customers satisfactions. zunTRAK provide the following solutions :
- Digital Marketing Solutions (mobile, internet) for enterprise/SMEs to help them promote/boost their business by generating leads, increasing sales and customers satisfactions.
- Telecom innovative solutions to help operators better their time to market and products and services portfolio
- Consultancy services for businesses: creates tactical programs to help businesses boost their bottom-line.
- Local business, products and service search engines for Africa region.
- Payments & cash-less solutions.
zunTRAK has a couple of subrands: KeloBridge: which is a digital marketing Offering zunSHOP: local business, products and services database and search engine Vision & Philosophy
The companys goal is to create long-term shareholder value by enhancing its position as a leading solution provider. The company’s philosophy focuses on end user experience through feedback, innovation, teamwork and integrity.
Something modern, cutting edge, but VERY professional. These are the pages required: HOME ABOUT US SERVICES OFFERING SOLUTIONS INDUSTRIES COVERED TECHNOLOGY & PARTNERS KELOBRIDGE KELOSHOP ZUNCAST
Blue
Grey / Silver
White / Black
left side
http://art.pictoquill.com/drafts/display/contest/118240/draft/3faa92c1d7e04b58a1c6f0d2b7e95a4c61830
http://art.pictoquill.com/drafts/display/contest/927615/draft/b81c44e09fa3d27c5e6018a9d4c7f2e390451
http://www.terubelmo.com/
Want something sleek, modern, cutting edge and professional. Open to suggestions. Will modify comments as I see a few websites come in. Love the modern look of our Logo designed attached. The website should be 2 languages: French and English. I have provided the menu in the 2 languages.

```html
<!DOCTYPE html>
<html lang="en">
<head>
<meta charset="utf-8">
<title>zunTRAK – Technology Solutions and Consulting</title>
<link href="https://fonts.googleapis.com/css2?family=Oswald:wght@500;700&family=Open+Sans:wght@300;400;600;700&display=swap" rel="stylesheet">
<style>
:root{
  --blue-deep:#0a3f86;
  --blue:#0f5fb8;
  --blue-bright:#2a8be0;
  --blue-light:#7fc0f5;
  --grey-bar:#e9ecef;
  --text:#3b3f44;
  --muted:#6c737b;
  --footer:#3a3b3d;
  --footer-dark:#2c2d2f;
  --white:#fff;
  --accent:#f2b21a;
}
*{box-sizing:border-box;margin:0;padding:0}
html,body{width:1200px;height:1067px;overflow:hidden;background:#fff}
body{font-family:"Open Sans",sans-serif;color:var(--text);position:relative}
.topbar{position:absolute;left:0;top:0;width:1200px;height:30px;background:var(--grey-bar);border-bottom:1px solid #cfd5db}
.topbar .welcome{position:absolute;left:183px;top:7px;font-size:11px;color:var(--muted);display:flex;align-items:center;gap:6px}
.topbar .home{width:14px;height:12px;background:var(--blue);display:inline-block}
.topbar .lang{position:absolute;right:80px;top:8px;font-size:11px;color:var(--muted);display:flex;gap:5px;align-items:center}
.flag{width:16px;height:11px;display:inline-block}
.logo-tab{position:absolute;left:487px;top:0;width:250px;height:100px;background:var(--white);border-radius:0 0 14px 14px;box-shadow:0 3px 10px rgba(0,0,0,.25);display:flex;align-items:center;justify-content:center;gap:10px;z-index:3}
.logo-tab .dot{width:30px;height:30px;border-radius:50%;background:var(--blue)}
.logo-tab .name{font-weight:700;font-size:32px;color:var(--blue-deep)}
.hero{position:absolute;left:0;top:30px;width:1200px;height:406px;background:radial-gradient(ellipse at 55% 40%,#1f79d0 0%,#0d4f9e 55%,#082e63 100%)}
.mainnav{position:absolute;left:183px;top:132px;width:200px;list-style:none}
.mainnav li{height:27px;border-bottom:1px solid rgba(255,255,255,.18);text-align:right;padding-right:12px;font-size:11px;line-height:27px;color:var(--blue-light);font-weight:600}
.mainnav li.active{color:var(--white);background:linear-gradient(90deg,transparent,rgba(255,255,255,.18))}
.hero-photo{position:absolute;left:790px;top:60px;width:330px;height:346px;background:linear-gradient(160deg,#d9e4ee 0%,#a9bfd6 45%,#2b5f9a 100%);border-radius:4px 4px 0 0;z-index:1}
.headline{position:absolute;left:502px;top:170px;width:320px;height:170px;color:var(--white);z-index:2}
.headline .big{font-family:"Oswald",sans-serif;font-weight:700;font-size:44px;line-height:46px;letter-spacing:1px}
.headline .and{position:absolute;left:238px;top:86px;font-size:24px;font-weight:300;color:var(--blue-light);line-height:24px}
.headline .consult{font-size:56px;font-weight:300;color:var(--blue-light);line-height:60px;margin-left:-3px;margin-top:8px}
.strip{position:absolute;left:0;top:436px;width:1200px;height:95px;background:linear-gradient(#1a7ad6,#0e5cb0)}
.strip .label{position:absolute;left:183px;top:0;width:200px;height:95px;background:var(--blue-bright);color:var(--white);font-family:"Oswald",sans-serif;font-size:19px;line-height:22px;text-align:center;padding-top:25px;font-weight:500}
.offers{position:absolute;left:400px;top:0;width:720px;height:95px;display:flex}
.offer{flex:1;text-align:center;color:var(--white);font-size:10px;font-weight:700;line-height:12px;padding-top:16px;border-left:1px solid rgba(255,255,255,.15)}
.offer svg{display:block;margin:0 auto 8px}
.content{position:absolute;left:183px;top:531px;width:937px;height:339px;display:flex;gap:24px;padding-top:18px}
.col h2{font-size:23px;font-weight:400;color:#2b2f33;margin-bottom:8px}
.col p{font-size:10px;line-height:14px;color:var(--muted)}
.col.about{width:310px}.col.team{width:250px}.col.board{width:330px}
.pic{height:96px;margin:10px 0;background:linear-gradient(135deg,#e7edf3,#9fb3c8);border-radius:2px}
.more{display:inline-block;margin-top:8px;background:var(--blue);color:var(--white);font-size:10px;padding:4px 12px;border-radius:2px}
.member{margin-bottom:10px}
.member h3{font-size:11px;font-weight:700;color:#2b2f33}
.member p{font-size:10px;line-height:13px}
.footer{position:absolute;left:0;top:870px;width:1200px;height:197px;background:var(--footer)}
.footer .links{position:absolute;left:183px;top:38px;width:360px;font-size:10px;line-height:16px;color:#cfd2d6}
.footer .copy{position:absolute;left:183px;top:88px;font-size:9px;color:#8c9096}
.social{position:absolute;left:183px;top:108px;display:flex;gap:4px}
.social span{width:16px;height:16px;border-radius:2px}
.contact{position:absolute;left:600px;top:0;width:200px;height:197px;background:var(--footer-dark);padding:14px 16px;color:#cfd2d6}
.footer h4{font-size:11px;font-weight:700;color:var(--white);letter-spacing:.5px;margin-bottom:10px}
.contact p{font-size:9px;line-height:13px;margin-bottom:8px}
.news{position:absolute;left:825px;top:14px;width:295px;color:#cfd2d6}
.news p{font-size:9px;line-height:13px;margin-bottom:8px}
.field{display:flex;align-items:center;font-size:9px;margin-bottom:5px}
.field span{width:60px}
.field i{flex:1;height:15px;background:#fff;border-radius:1px}
.subscribe{margin-left:60px;display:inline-block;background:var(--accent);color:#2b2b2b;font-size:9px;font-weight:700;padding:3px 10px;border-radius:2px}
</style>
</head>
<body>
<header class="topbar">
  <div class="welcome"><span class="home"></span>Welcome to zunTRAK</div>
  <div class="lang">Language
    <svg class="flag" viewBox="0 0 16 11"><rect width="16" height="11" fill="#1b3f8f"/><path d="M0 0L16 11M16 0L0 11" stroke="#fff" stroke-width="2"/><path d="M8 0V11M0 5.5H16" stroke="#fff" stroke-width="3"/><path d="M8 0V11M0 5.5H16" stroke="#c8102e" stroke-width="1.6"/></svg>
    <svg class="flag" viewBox="0 0 16 11"><rect width="5.3" height="11" fill="#1d3f9a"/><rect x="5.3" width="5.4" height="11" fill="#fff"/><rect x="10.7" width="5.3" height="11" fill="#d52b1e"/></svg>
  </div>
</header>
<div class="logo-tab"><span class="dot"></span><span class="name">zunTRAK</span></div>

<section class="hero">
  <ul class="mainnav">
    <li class="active">ABOUT US</li><li>SERVICES OFFERING</li><li>SOLUTIONS</li><li>INDUSTRIES COVERED</li><li>TECHNOLOGY &amp; PARTNERS</li><li>KELOBRIDGE</li><li>KELOSHOP</li><li>ZUNCAST</li>
  </ul>
  <div class="hero-photo" role="img" aria-label="Businesswoman in a suit talking on the phone"></div>
  <div class="headline">
    <div class="big">TECHNOLOGY<br>SOLUTIONS</div>
    <span class="and">and</span>
    <div class="consult">Consulting</div>
  </div>
</section>

<section class="strip">
  <div class="label">SERVICE &amp;<br>SOLUTION OFFERING</div>
  <div class="offers">
    <div class="offer"><svg width="30" height="30" viewBox="0 0 30 30" fill="none" stroke="#fff" stroke-width="2"><rect x="9" y="3" width="12" height="24" rx="2"/><path d="M13 23h4"/></svg>TELECOM<br>SOLUTIONS</div>
    <div class="offer"><svg width="30" height="30" viewBox="0 0 30 30" fill="none" stroke="#fff" stroke-width="2"><circle cx="15" cy="15" r="11"/><circle cx="15" cy="15" r="4"/></svg>TECHNOLOGY<br>CONSULTING</div>
    <div class="offer"><svg width="30" height="30" viewBox="0 0 30 30" fill="none" stroke="#fff" stroke-width="2"><rect x="4" y="6" width="22" height="15" rx="1"/><path d="M10 26h10M15 21v5"/></svg>VENDOR<br>SPECIFIC SOLUTIONS</div>
    <div class="offer"><svg width="30" height="30" viewBox="0 0 30 30" fill="none" stroke="#fff" stroke-width="2"><path d="M5 25l12-12M17 5a6 6 0 1 0 8 8"/></svg>CUSTOMIZED<br>SOLUTIONS</div>
    <div class="offer"><svg width="30" height="30" viewBox="0 0 30 30" fill="none" stroke="#fff" stroke-width="2"><rect x="3" y="4" width="10" height="9"/><rect x="17" y="17" width="10" height="9"/><path d="M13 8h8v9"/></svg>SYSTEMS<br>INTEGRATION</div>
    <div class="offer"><svg width="30" height="30" viewBox="0 0 30 30" fill="none" stroke="#fff" stroke-width="2"><circle cx="15" cy="10" r="5"/><path d="M5 27c1-7 19-7 20 0"/></svg>SKILL<br>OUTSOURCING</div>
  </div>
</section>

<main class="content">
  <article class="col about">
    <h2>About zunTRAK</h2>
    <p>zunTRAK is an integrated business development solution company that provides technology integration.</p>
    <div class="pic" role="img" aria-label="Business people at work in an office"></div>
    <p>Integration, advisory services, infrastructure to enterprises and SME to boost their leads, sales and customers satisfactions across the region.</p>
    <span class="more">Read More ›</span>
  </article>
  <article class="col team">
    <h2>Our Team</h2>
    <p>zunTRAK comprises architects, designers, practitioners, managers and leaders.</p>
    <div class="pic" role="img" aria-label="Team of colleagues meeting around a table"></div>
    <p>Their competence, professional standing and energy. They have been recruited on the basis of the quality and breadth of their experience.</p>
    <span class="more">Read More ›</span>
  </article>
  <article class="col board">
    <h2>Board of Directors</h2>
    <div class="member"><h3>MORVITH TIENDREBE</h3><p>Executive President, Alvern School Graduate<br>Norel Faso – Telecommunication &amp; Information Technology and Services</p></div>
    <div class="member"><h3>DAREL MOUSSO</h3><p>Managing Partner, Quilmar Consulting<br>Agency – Information Technology and Services</p></div>
    <div class="member"><h3>VERAN OSTIK</h3><p>Mobile Marketing Expert<br>Vendor – Telecommunication &amp; Information Technology and Services</p></div>
    <div class="member"><h3>SEDRIN PALOU</h3><p>Owner &amp; CEO, Brevona Group<br>Norel Faso – Information Technology and Services</p></div>
  </article>
</main>

<footer class="footer">
  <div class="links">Home &nbsp;|&nbsp; About Us &nbsp;|&nbsp; Services Offering &nbsp;|&nbsp; Solutions &nbsp;|&nbsp; Industries Covered<br>Technology &amp; Partners &nbsp;|&nbsp; KeloBridge &nbsp;|&nbsp; zunSHOP &nbsp;|&nbsp; ZUNCAST</div>
  <div class="copy">Copyright © 2013 zuntrak.net. All Rights Reserved</div>
  <div class="social"><span style="background:#3b5998"></span><span style="background:#29a9e1"></span><span style="background:#d34836"></span></div>
  <div class="contact">
    <h4>CONTACT US</h4>
    <p>zunTRAK SARL<br>Boulevard Central, Avenue 12<br>Email: hello@zuntrak.net</p>
    <p>Phone: +226 50 41 27 63<br>Fax: +226 50 41 27 64</p>
  </div>
  <div class="news">
    <h4>SUBSCRIBE TO OUR NEWSLETTER</h4>
    <p>Enter your details to receive our latest news, updates and offers about our solutions and services.</p>
    <div class="field"><span>Name</span><i></i></div>
    <div class="field"><span>Email</span><i></i></div>
    <div class="field"><span>Profession</span><i></i></div>
    <span class="subscribe">Subscribe</span>
  </div>
</footer>
</body>
</html>
```